Cybersecurity company is looking for business card.

I need a business card design for our company, we are a cybersecurity company providing advance technology to protect agains any kind of malware. We need a fresh modern design it should communicate modern, technology and growth.

Target Market(s)

Business to business

Industry/Entity Type

Business

Contact Information for Business Card

Should have location, address, fax, mobile, phone, email and website.

Requirements
Must have
• Must follow company's logo color and style. Must have the company's log on its.

```html
<!DOCTYPE html>
<html lang="en">
<head>
<meta charset="utf-8">
<title>Veltrix Business Card</title>
<link rel="stylesheet" href="https://fonts.googleapis.com/css2?family=Exo+2:wght@700&family=Open+Sans:wght@600&display=swap">
<style>
  :root {
    --ink: #000000;
    --crimson: #a00d0e;
    --paper: #ffffff;
    --stage-center: #ffffff;
    --stage-edge: #e6e6e6;
    --frame: #3a3a3a;
  }
  html, body {
    margin: 0;
    padding: 0;
    width: 1200px;
    height: 1001px;
    overflow: hidden;
  }
  .stage {
    position: relative;
    width: 1200px;
    height: 1001px;
    box-sizing: border-box;
    border: 2px solid var(--frame);
    background: radial-gradient(ellipse at 50% 50%, var(--stage-center) 0%, var(--stage-edge) 75%);
  }
  .card-art {
    position: absolute;
    left: 0;
    top: 0;
  }
  .brand-name {
    position: absolute;
    margin: 0;
    font-family: "Exo 2", sans-serif;
    font-weight: 700;
    font-size: 46px;
    line-height: 1;
    letter-spacing: 0.5px;
    color: var(--paper);
    transform: translate(-50%, -50%);
    white-space: nowrap;
  }
  .brand-name.front { left: 463px; top: 284px; }
  .brand-name.back  { left: 598px; top: 721px; }
  .contact {
    position: absolute;
    margin: 0;
    font-family: "Open Sans", sans-serif;
    font-weight: 600;
    font-size: 15.5px;
    line-height: 1;
    color: var(--paper);
    white-space: nowrap;
  }
  .contact-icon {
    position: absolute;
  }
</style>
</head>
<body>
<div class="stage">

  <svg class="card-art" width="1200" height="1001" viewBox="0 0 1200 1001" aria-hidden="true">
    <defs>
      <clipPath id="front-shape">
        <rect x="303" y="127" width="590" height="328" rx="40" ry="40"/>
      </clipPath>
      <clipPath id="back-shape">
        <rect x="303" y="568" width="590" height="328" rx="40" ry="40"/>
      </clipPath>
    </defs>

    <!-- front card -->
    <g clip-path="url(#front-shape)">
      <rect x="303" y="127" width="590" height="328" fill="var(--ink)"/>
      <rect x="596" y="127" width="297" height="328" fill="var(--crimson)"/>
      <path d="M303 205 H308 Q322 205 322 219 V366 Q322 380 308 380 H303 Z" fill="var(--crimson)"/>
      <path d="M596 205 H601 Q615 205 615 219 V366 Q615 380 601 380 H596 Z" fill="var(--ink)"/>
    </g>

    <!-- back card -->
    <g clip-path="url(#back-shape)">
      <rect x="303" y="568" width="590" height="328" fill="var(--ink)"/>
      <rect x="303" y="837" width="590" height="59" fill="var(--crimson)"/>
      <path d="M508 837 H684 V845 Q684 857 672 857 H520 Q508 857 508 845 Z" fill="var(--ink)"/>
    </g>
    <path d="M510 566 H686 V568 Q686 587 667 587 H529 Q510 587 510 568 Z" fill="var(--crimson)"/>

    <!-- contact icons -->
    <g fill="none" stroke="var(--paper)" stroke-width="1.6">
      <rect x="680" y="165" width="10" height="20" rx="1.5"/>
      <line x1="683" y1="182" x2="687" y2="182"/>
      <rect x="677" y="272" width="17" height="12"/>
      <polyline points="677,272 685.5,279 694,272"/>
    </g>
    <path d="M682 199 q-3 2 -1 8 q3 7 9 11 q4 2 6 -1 l-3 -3 q-2 1 -3 0 q-3 -2 -5 -6 q-1 -2 1 -3 z" fill="var(--paper)"/>
    <path d="M685 370 l-9 8 h3 v9 h4 v-5 h4 v5 h4 v-9 h3 z" fill="var(--paper)"/>
  </svg>

  <p class="brand-name front">veltrix</p>
  <p class="brand-name back">veltrix</p>

  <p class="contact" style="left:705px; top:169px;">414-372-19</p>
  <p class="contact" style="left:705px; top:203px;">414-830-57</p>
  <p class="contact" style="left:673px; top:237px;">fax: 414-615-92</p>
  <p class="contact" style="left:708px; top:270px;">nora@veltrixsec.com</p>
  <p class="contact" style="left:710px; top:299px;">www.veltrixsec.io</p>
  <p class="contact" style="left:703px; top:373px;">318 8th avenue</p>
  <p class="contact" style="left:704px; top:402px;">75011 Paris, France</p>

</div>
</body>
</html>
```